Intermodal Trucking Company Website

My client is a trucking company that takes the containers you see on the back of a ship or railroad car and delivers them in the midwestern part of the United States. Here are some of their competitors Websites and their logo to use as part of the design.

http://www.vardenhollow.example/
https://www.pelrix.example/
http://www.brackwaterfreightlines.example/
https://www.mbv-lo.example/

Industry/Entity Type

Trucking Company

Number of Pages Required

2 page

Requirements
Must have
• Website must be professional and the design needs to be suitable for a responsive Website.
Should not have
• Please do not submit designs with misspellings. Designs with misspellings will be eliminated.

```html
<!DOCTYPE html>
<html lang="en">
<head>
<meta charset="utf-8">
<title>Ironvale Haulage — Intermodal Trucking</title>
<link href="https://fonts.googleapis.com/css2?family=Lato:wght@400;700;900&family=Roboto:wght@400;500;700&display=swap" rel="stylesheet">
<style>
:root{
  --orange:#d9512c;
  --yellow:#fcc930;
  --ink:#1d1d1d;
  --body:#777;
  --muted:#999;
  --line:#e2e2e2;
  --footer:#2b2b2b;
  --white:#fff;
}
*{box-sizing:border-box;margin:0;padding:0}
html,body{width:671px;height:1200px;overflow:hidden}
body{position:relative;background:var(--white);font-family:"Roboto",Arial,sans-serif;color:var(--body)}
.abs{position:absolute}

/* header */
.contact-line{top:8px;font-size:7px;color:#666;display:flex;align-items:center;gap:3px;white-space:nowrap}
.contact-line svg{width:7px;height:7px}
.social-top{top:8px;left:480px;display:flex;gap:8px}
.social-top span{width:7px;height:7px;border-radius:50%;background:#9a9a9a;display:block}
.brand{left:86px;top:16px;width:80px;font-family:"Lato",sans-serif;font-weight:900;font-size:13px;line-height:14px;color:var(--orange);text-align:center}
.navband{left:0;top:26px;width:671px;height:49px}
.nav{top:26px;left:0;width:671px;height:49px;font-family:"Roboto",sans-serif;font-weight:500;font-size:9.6px;line-height:12px;color:var(--white)}
.nav a{color:inherit;text-decoration:none;position:absolute;top:19px;white-space:nowrap}
.nav svg{position:absolute;top:20px}

/* hero */
.hero{left:0;top:75px;width:671px;height:255px;background:linear-gradient(160deg,#5a4a3a 0%,#8a6a45 35%,#b97a3d 60%,#3a2c22 100%)}
.hero-title{left:0;top:148px;width:671px;text-align:center;font-family:"Lato",sans-serif;font-weight:700;font-size:23px;line-height:29px;color:var(--white);letter-spacing:-.3px}
.btn-quote{left:299px;top:212px;width:73px;height:23px;background:var(--yellow);border-radius:2px;font-family:"Lato",sans-serif;font-weight:700;font-size:7.5px;color:var(--ink);display:flex;align-items:center;justify-content:center}
.hero-arrow{width:20px;height:24px;display:flex;align-items:center;justify-content:center}

/* services */
.service-ring{width:144px;height:144px;border-radius:50%;background:#d8d8d8;top:264px}
.service-photo{position:absolute;left:8px;top:8px;width:128px;height:128px;border-radius:50%}
.service-title{top:412px;width:158px;text-align:center;font-family:"Lato",sans-serif;font-weight:700;font-size:7.5px;color:var(--orange);white-space:nowrap}
.service-text{top:428px;width:158px;text-align:center;font-size:6.2px;line-height:10.4px;color:var(--muted)}
.read-more{top:467px;width:158px;text-align:center;font-size:5.6px;font-weight:700;color:#666}
.pager{top:502px;left:284px;display:flex;align-items:center;gap:4px}
.pager i{display:block;width:38px;height:1px;background:var(--line)}
.pager b{display:flex;width:17px;height:17px;background:#e4e4e4;align-items:center;justify-content:center;color:#fff;font-size:8px}

/* why */
.why{left:0;top:533px;width:671px;height:244px;background:var(--yellow)}
.why-truck{left:0;top:541px;width:320px;height:222px;background:radial-gradient(ellipse at 45% 50%,#f4f4f4 0%,#d6d6d6 55%,rgba(200,160,40,0) 75%)}
.why-title{left:346px;top:559px;font-family:"Lato",sans-serif;font-weight:700;font-size:24px;color:var(--orange);letter-spacing:-.5px;white-space:nowrap}
.why-item{left:347px;width:235px}
.why-item h3{font-family:"Lato",sans-serif;font-weight:700;font-size:9.6px;color:var(--ink);display:flex;align-items:center;gap:5px;white-space:nowrap}
.why-item p{margin-left:13px;margin-top:3px;font-size:7px;line-height:9px;color:var(--ink)}

/* news */
.news-title{left:0;top:803px;width:671px;text-align:center;font-family:"Lato",sans-serif;font-weight:700;font-size:24px;color:var(--orange);letter-spacing:-.5px}
.news-intro{left:0;top:833px;width:671px;text-align:center;font-size:6.6px;line-height:11px;color:#666}
.news-card{top:874px;width:157px}
.news-photo{width:157px;height:101px}
.news-card h4{margin-top:5px;font-family:"Lato",sans-serif;font-weight:400;font-size:11.4px;color:var(--ink);white-space:nowrap}
.news-date{margin-top:2px;font-size:6.6px;color:var(--orange)}
.news-card p{margin-top:7px;width:152px;font-size:6.8px;line-height:11.6px;color:#666}

/* footer */
.footer{left:0;top:1088px;width:671px;height:112px;background:var(--footer)}
.foot-head{top:1104px;font-family:"Lato",sans-serif;font-weight:700;font-size:9.6px;color:var(--white);white-space:nowrap}
.foot-text{font-size:7.4px;line-height:13.4px;color:#e6e6e6}
.news-form{left:312px;top:1155px;width:141px;height:18px;background:var(--white);display:flex;align-items:center;justify-content:space-between;padding:0 2px 0 6px;font-size:6.4px;color:#999}
.news-form b{background:var(--orange);color:var(--white);font-weight:500;font-size:6.4px;padding:3px 5px}
.foot-social{top:1124px;left:473px;display:flex;gap:5px}
.foot-social span{width:19px;height:19px;border-radius:50%;background:var(--white);display:block}
</style>
</head>
<body>

<!-- header -->
<div class="abs brand">Ironvale<br>Haulage</div>
<div class="abs contact-line" style="left:182px">
  <svg viewBox="0 0 10 10"><path d="M2 1l2 2-1 1.5c.6 1.3 1.2 1.9 2.5 2.5L7 6l2 2-1.5 1.5C4 9 1 6 .5 2.5z" fill="#888"/></svg>
  Phone: (+1) 0100-555-014
</div>
<div class="abs contact-line" style="left:286px">
  <svg viewBox="0 0 10 10"><rect x="1" y="2" width="8" height="6" fill="#888"/><path d="M1 2l4 3 4-3" stroke="#fff" fill="none"/></svg>
  Email: hello@ironvale.example
</div>
<div class="abs social-top" aria-label="Social links"><span></span><span></span><span></span><span></span><span></span><span></span><span></span></div>

<svg class="abs navband" viewBox="0 0 671 49" preserveAspectRatio="none" aria-hidden="true">
  <polygon points="190,0 671,0 671,49 150,49" fill="var(--orange)"/>
</svg>
<nav class="abs nav">
  <a style="left:197px">HOME</a>
  <a style="left:247px">ABOUT US</a>
  <a style="left:317px">SERVICES</a>
  <a style="left:385px">SHOP</a>
  <a style="left:436px">NEWS</a>
  <a style="left:489px">CONTACT</a>
  <svg style="left:549px" width="10" height="10" viewBox="0 0 10 10"><circle cx="4" cy="4" r="3" stroke="#fff" stroke-width="1.6" fill="none"/><path d="M6.3 6.3L9 9" stroke="#fff" stroke-width="1.8"/></svg>
</nav>

<!-- hero -->
<div class="abs hero" role="img" aria-label="Freight train carrying shipping containers at sunset"></div>
<h1 class="abs hero-title">IRONVALE HAULAGE<br>IS MORE THAN JUST TRUCKING.</h1>
<div class="abs btn-quote">GET QUOTE</div>
<div class="abs hero-arrow" style="left:56px;top:189px">
  <svg width="10" height="12" viewBox="0 0 10 12"><path d="M8 1L3 6l5 5" stroke="#fff" stroke-width="2.6" fill="none"/></svg>
</div>
<div class="abs hero-arrow" style="left:590px;top:189px;background:#2a2a2a">
  <svg width="10" height="12" viewBox="0 0 10 12"><path d="M2 1l5 5-5 5" stroke="#fff" stroke-width="2.6" fill="none"/></svg>
</div>

<!-- services -->
<div class="abs service-ring" style="left:93px"><div class="service-photo" role="img" aria-label="Row of parked truck cabs" style="background:linear-gradient(180deg,#d7d3e8 0%,#b8c2d4 45%,#6d7486 70%,#9c9890 100%)"></div></div>
<div class="abs service-ring" style="left:263px"><div class="service-photo" role="img" aria-label="Warehouse workers beside a forklift" style="background:linear-gradient(180deg,#7d8794 0%,#a9b0b8 40%,#c9b94a 70%,#3b3b3b 100%)"></div></div>
<div class="abs service-ring" style="left:434px"><div class="service-photo" role="img" aria-label="Container ship at a lit port at dusk" style="background:linear-gradient(180deg,#4a4fb0 0%,#7b5aa8 40%,#d08a4a 65%,#1d3f66 100%)"></div></div>

<div class="abs service-title" style="left:86px">PACKAGING &amp; STORAGE</div>
<div class="abs service-title" style="left:256px">CONTRACT LOGISTICS</div>
<div class="abs service-title" style="left:427px">SAFETY &amp; RELIABILITY</div>

<p class="abs service-text" style="left:86px">Quisque ligulas ipsum, euismod atras vulputate iltricies etri elit. Class aptent taciti sociosqu ad litora torquent per conubia nostra, per inceptos himenaeos. Nulla...</p>
<p class="abs service-text" style="left:256px">Quisque ligulas ipsum, euismod atras vulputate iltricies etri elit. Class aptent taciti sociosqu ad litora torquent per conubia nostra, per inceptos himenaeos. Nulla...</p>
<p class="abs service-text" style="left:427px">Quisque ligulas ipsum, euismod atras vulputate iltricies etri elit. Class aptent taciti sociosqu ad litora torquent per conubia nostra, per inceptos himenaeos. Nulla...</p>

<div class="abs read-more" style="left:86px">READ MORE →</div>
<div class="abs read-more" style="left:256px">READ MORE →</div>
<div class="abs read-more" style="left:427px">READ MORE →</div>

<div class="abs pager"><i></i><b>‹</b><b>›</b><i></i></div>

<!-- why choose us -->
<div class="abs why"></div>
<div class="abs why-truck" role="img" aria-label="White semi truck with trailer"></div>
<h2 class="abs why-title">WHY CHOOSE US</h2>
<div class="abs why-item" style="top:600px">
  <h3><svg width="8" height="8" viewBox="0 0 8 8"><path d="M0 0l8 4-8 4 2-4z" fill="#1d1d1d"/></svg>FAST TRANSPORTATION SERVICE</h3>
  <p>Lorem ipsum dolor sit amet, consectetur adipiscing elit, sed do eiusmod tempor incididunt ut labore et dolore.</p>
</div>
<div class="abs why-item" style="top:649px">
  <h3><svg width="8" height="8" viewBox="0 0 8 8"><path d="M0 0l8 4-8 4 2-4z" fill="#1d1d1d"/></svg>SAFETY AND RELIABILITY</h3>
  <p>Lorem ipsum dolor sit amet, consectetur adipiscing elit, sed do eiusmod tempor incididunt ut labore et dolore.</p>
</div>
<div class="abs why-item" style="top:701px">
  <h3><svg width="8" height="8" viewBox="0 0 8 8"><path d="M0 0l8 4-8 4 2-4z" fill="#1d1d1d"/></svg>SHIPPING WORLDWIDE</h3>
  <p>Lorem ipsum dolor sit amet, consectetur adipiscing elit, sed do eiusmod tempor incididunt ut labore et dolore.</p>
</div>

<!-- latest news -->
<h2 class="abs news-title">LATEST NEWS</h2>
<p class="abs news-intro">Lorem ipsum dolor sit amet, consectetur adipiscing elit. Pellent esque dignissim<br>eros a sapien tempus, ut eleifend neque convallis.empor incididunt ut</p>

<article class="abs news-card" style="left:90px">
  <div class="news-photo" role="img" aria-label="White delivery truck at a loading dock" style="background:linear-gradient(180deg,#6b4a3a 0%,#cfcfcf 45%,#e8e8e8 70%,#7a6a5a 100%)"></div>
  <h4>Northline Parcel Service</h4>
  <div class="news-date">April 28, 2016</div>
  <p>Lorem ipsum dolor sit amet, consectetuer adipiscing elit, sed diam nonummy nibh euismod tincidunt ut laoreet dolore magna aliquam erat volutpat.</p>
</article>
<article class="abs news-card" style="left:258px">
  <div class="news-photo" role="img" aria-label="Black truck hauling a white trailer under blue sky" style="background:linear-gradient(180deg,#5f9ad8 0%,#a9cbe9 35%,#e6e6e6 60%,#3a3a3a 100%)"></div>
  <h4>Best Trucking Companies</h4>
  <div class="news-date">April 28, 2016</div>
  <p>Lorem ipsum dolor sit amet, consectetuer adipiscing elit, sed diam nonummy nibh euismod tincidunt ut laoreet dolore magna aliquam erat volutpat.</p>
</article>
<article class="abs news-card" style="left:426px">
  <div class="news-photo" role="img" aria-label="Red truck on a desert highway with mesas" style="background:linear-gradient(180deg,#8fb2d6 0%,#a07a6a 40%,#b0354a 65%,#6d6d6d 100%)"></div>
  <h4>Halvorsen Trucking Company</h4>
  <div class="news-date">April 28, 2016</div>
  <p>Lorem ipsum dolor sit amet, consectetuer adipiscing elit, sed diam nonummy nibh euismod tincidunt ut laoreet dolore magna aliquam erat volutpat.</p>
</article>

<!-- footer -->
<footer class="abs footer"></footer>
<div class="abs foot-head" style="left:90px">Our Address</div>
<div class="abs foot-text" style="left:90px;top:1125px">Westbrook<br>42 Larchmere Ave, Westbrook,<br>ON K0X 1A1 &nbsp;1 800 555-0190</div>
<div class="abs foot-head" style="left:230px">Company</div>
<div class="abs foot-text" style="left:231px;top:1125px;font-size:7px">About Us<br>Current Projects<br>Get Involved<br>Contact Us</div>
<div class="abs foot-head" style="left:312px">Sign up for newsletter</div>
<div class="abs foot-text" style="left:312px;top:1125px;font-size:6.4px;line-height:9.6px;width:150px">Claritas est etiam processus dynamicus, qui sequitur mutationem consuetudium lectorum.</div>
<div class="abs news-form"><span>Enter Your Email...</span><b>SIGN UP</b></div>
<div class="abs foot-head" style="left:475px">Connect with Us</div>
<div class="abs foot-social" aria-label="Social links"><span></span><span></span><span></span><span></span></div>
<div class="abs foot-text" style="left:474px;top:1146px;font-size:5.4px">© 2017 Ironvale Haulage</div>

</body>
</html>
```